Sports Psychology Business Card Design

Need a catchy and unique business card design for our sport psychology practice. We provide mental performance counseling and consulting to performers from all types of industries with a special emphases on athletes.The name of our practice is "Steady Core of Achievement" or "SCA" as is indicated in the logo examples submitted in this brief. Also provided were logos with specific sports referenced which represent sources of our clients from those sports.

Target Market(s)

Executives, Professionals (doctors, lawyers, etc.), Athletes, Entertainers and other performers

Contact Information for Business Card

Need to include our logo (logos provided in this brief).

Font styles to use
Other font styles liked:
• Font can be found in logo

Colors
0792cd
34a7d8
85cae6

Requirements
Must have
• Our logo and reference to our provision of mental performance counseling/consulting/coaching
Nice to have
• References to sports that our athletes play as provided in the brief.
Should not have
• This is not a general wellness consulting practice. Our focus is on consulting to improve mental performance.

```html
<!DOCTYPE html>
<html lang="en">
<head>
<meta charset="utf-8">
<title>Steady Core of Achievement – Business Cards</title>
<link href="https://fonts.googleapis.com/css2?family=Michroma&display=swap" rel="stylesheet">
<style>
  :root {
    --page-bg: #ffffff;
    --blue-top: #2f98d6;
    --blue-bottom: #86cbea;
    --silver-top: #a39e96;
    --silver-bottom: #e6e8e8;
    --band-blue: #0b72bf;
    --band-dark: #292d30;
    --band-taupe: #938d82;
    --mark-dark: #2a2e31;
    --text-light: #ffffff;
  }
  * { margin: 0; padding: 0; box-sizing: border-box; }
  html, body {
    width: 1200px;
    height: 900px;
    overflow: hidden;
    background: var(--page-bg);
  }
  .canvas {
    position: relative;
    width: 1200px;
    height: 900px;
  }
  .card {
    position: absolute;
    top: 180px;
    width: 318px;
    height: 556px;
    overflow: hidden;
    font-family: "Michroma", "Arial", sans-serif;
  }
  .card--blue {
    left: 263px;
    background:
      repeating-linear-gradient(115deg, rgba(255,255,255,0.05) 0 2px, rgba(255,255,255,0) 2px 7px),
      linear-gradient(160deg, var(--blue-top), var(--blue-bottom));
  }
  .card--silver {
    left: 640px;
    background:
      repeating-linear-gradient(115deg, rgba(255,255,255,0.05) 0 2px, rgba(255,255,255,0) 2px 7px),
      linear-gradient(160deg, var(--silver-top), var(--silver-bottom));
  }
  .card__tagline {
    position: absolute;
    top: 64px;
    left: 0;
    width: 100%;
    text-align: center;
    color: var(--text-light);
    font-size: 16px;
    line-height: 22px;
    letter-spacing: 0.5px;
    text-transform: uppercase;
  }
  .card__wordmark {
    position: absolute;
    top: 192px;
    left: 0;
    width: 100%;
    text-align: center;
    color: var(--mark-dark);
    font-size: 74px;
    line-height: 90px;
    letter-spacing: 2px;
  }
  .sport-band {
    position: absolute;
    left: 0;
    width: 100%;
    height: 39px;
    display: flex;
    align-items: center;
    justify-content: center;
    color: var(--text-light);
    font-size: 13px;
    letter-spacing: 0.3px;
    text-transform: uppercase;
  }
  .sport-band--first { top: 423px; }
  .sport-band--second { top: 468px; }
  .sport-band--third { top: 513px; height: 40px; }
  .card--blue .sport-band--accent { background: var(--band-blue); }
  .card--silver .sport-band--accent { background: var(--band-taupe); }
  .sport-band--dark { background: var(--band-dark); }
</style>
</head>
<body>
<main class="canvas">
  <section class="card card--blue">
    <p class="card__tagline">Steady Core of<br>Achievement</p>
    <p class="card__wordmark">SCA</p>
    <div class="sport-band sport-band--first sport-band--accent">Softball</div>
    <div class="sport-band sport-band--second sport-band--dark">Basketball</div>
    <div class="sport-band sport-band--third sport-band--accent">Baseball</div>
  </section>

  <section class="card card--silver">
    <p class="card__tagline">Steady Core of<br>Achievement</p>
    <p class="card__wordmark">SCA</p>
    <div class="sport-band sport-band--first sport-band--accent">Softball</div>
    <div class="sport-band sport-band--second sport-band--dark">Basketball</div>
    <div class="sport-band sport-band--third sport-band--accent">Baseball</div>
  </section>
</main>
</body>
</html>
```